Lar Ventura Banners Ads

We need to create 4 animated banners ads in GIF (3 arts for each banner) to Lar Ventura Publinet Display Campaign
Lar Ventura is an ecommerce in Brazil that sells high end home products.
It is a Branding Campaign, but we will add products images on it, so it has to be very sofisticated like the brand is.

We need 4 designs - 1 design for each size:

- Retângulo inline (300 X 250)
- Retângulo grande (336 x 280)
- Banner (468 x 60)
- Cabeçalho (728 x 90)

Please, find the briefing in pdf archive attached

Text we can work on th banners:

1 - Sofisticação com exclusividade para sua Casa!
2 - chique, exclusivo e encantador
3 - Encantador, sofisticado e exclusivo

The final image has to have Tecelmar´s Logo, Lar Ventura´s logo and a call to action:

Confira nossos produtos exclusivos!

_________________________________________________________________
UPDATE

Please, for the colors, take the ones from pdf; (use more collors chics, silver and white, but not only this colors);
Don't forget the CALL TO ACTION " Confira nossos Produtos Exclusivos!"

If you'd like to meet the brand and the target, here is the page on Exemplorede: https://www.exemplorede.com/LarVenturaHomeVentura

But please, DO NOT COPY ANY OF THESE EXAMPLES ON THE PAGE.
We need something more executive.

Target Market(s)

Woman 30+
Trendy, modern, sofisticated, married or mum, cosmopolitan,
UPPERCLASS

Industry/Entity Type

Call

Font styles to use
Script
Other font styles liked:
• BrindleTrial

Requirements
Must have
• Product images
Text
Product Image + Call to action on final layer with logos
As you will see the example in pdf archive attached
Nice to have
• frames
Should not have
• people
flowers
girlish drawing

```html
<!DOCTYPE html>
<html lang="pt-BR">
<head>
<meta charset="utf-8">
<title>Lar Ventura – Banners Display</title>
<link rel="stylesheet" href="https://fonts.googleapis.com/css2?family=Archivo:wght@500;700&display=swap">
<style>
  :root {
    --stage: #ece7e1;
    --white: #ffffff;
    --silver: #d3d3d0;
    --silver-deep: #bfbfbb;
    --ink: #111111;
    --logo: #8c8277;
    --cta: #e0439b;
    --cta-text: #ffffff;
    --photo-a: #c9cac8;
    --photo-b: #a9b6c4;
    --photo-c: #6b5443;
  }
  * { box-sizing: border-box; margin: 0; padding: 0; }
  html, body { width: 1200px; height: 900px; overflow: hidden; }
  body {
    background: var(--stage);
    font-family: "Archivo", Arial, sans-serif;
    position: relative;
  }
  .ad {
    position: absolute;
    overflow: hidden;
    background: var(--white);
    transform-origin: top left;
    transform: scale(1.172);
    box-shadow: 0 2px 6px rgba(0,0,0,.12);
  }
  .ad > * { position: absolute; }
  .logo {
    color: var(--logo);
    font-weight: 700;
    font-variant: small-caps;
    letter-spacing: .04em;
    white-space: nowrap;
    line-height: 1;
  }
  .silver-arc { background: var(--silver); border-radius: 50%; }
  .product-photo {
    background: linear-gradient(160deg, var(--photo-a) 0%, var(--photo-b) 55%, var(--photo-c) 100%);
  }
  .headline {
    color: var(--ink);
    font-weight: 700;
    text-align: center;
    line-height: 1.3;
  }
  .cta {
    background: var(--cta);
    color: var(--cta-text);
    font-weight: 700;
    text-align: center;
    line-height: 1;
    display: flex;
    flex-direction: column;
    justify-content: center;
  }

  /* Cabeçalho 728 x 90 */
  .ad-leaderboard { left: 168px; top: 214px; width: 728px; height: 90px; }
  .ad-leaderboard .logo { left: 8px; top: 32px; font-size: 27px; }
  .ad-leaderboard .silver-arc { left: 192px; top: -120px; width: 900px; height: 330px; }
  .ad-leaderboard .product-photo { left: 530px; top: 0; width: 198px; height: 90px;
    -webkit-mask: linear-gradient(90deg, transparent, #000 25%); mask: linear-gradient(90deg, transparent, #000 25%); }
  .ad-leaderboard .cta { left: 195px; top: 33px; width: 189px; height: 30px; border-radius: 8px; font-size: 13px; }
  .ad-leaderboard .headline { left: 385px; top: 17px; width: 150px; font-size: 15px; }

  /* Banner 468 x 60 */
  .ad-banner { left: 320px; top: 355px; width: 468px; height: 60px; }
  .ad-banner .logo { left: 5px; top: 22px; font-size: 18px; }
  .ad-banner .silver-arc { left: 118px; top: -80px; width: 600px; height: 220px; }
  .ad-banner .product-photo { left: 340px; top: 0; width: 128px; height: 60px;
    -webkit-mask: linear-gradient(90deg, transparent, #000 25%); mask: linear-gradient(90deg, transparent, #000 25%); }
  .ad-banner .cta { left: 126px; top: 22px; width: 120px; height: 21px; border-radius: 6px; font-size: 8.5px; }
  .ad-banner .headline { left: 248px; top: 10px; width: 94px; font-size: 9.5px; }

  /* Retângulo inline 300 x 250 */
  .ad-inline { left: 320px; top: 517px; width: 300px; height: 250px; }
  .ad-inline .logo { left: 0; width: 300px; text-align: center; top: 4px; font-size: 36px; }
  .ad-inline .silver-arc { left: -160px; top: 40px; width: 560px; height: 460px; }
  .ad-inline .product-photo { left: 150px; top: 95px; width: 150px; height: 155px;
    -webkit-mask: linear-gradient(180deg, transparent, #000 20%); mask: linear-gradient(180deg, transparent, #000 20%); }
  .ad-inline .headline { left: 20px; top: 76px; width: 170px; font-size: 16px; }
  .ad-inline .cta { left: 0; top: 221px; width: 182px; height: 29px; border-radius: 0 8px 8px 0; font-size: 12px; }

  /* Retângulo grande 336 x 280 */
  .ad-large { left: 744px; top: 499px; width: 336px; height: 280px; }
  .ad-large .logo { left: 0; width: 336px; text-align: center; top: 3px; font-size: 42px; }
  .ad-large .silver-arc { left: -180px; top: 44px; width: 630px; height: 510px; }
  .ad-large .product-photo { left: 170px; top: 105px; width: 166px; height: 175px;
    -webkit-mask: linear-gradient(180deg, transparent, #000 20%); mask: linear-gradient(180deg, transparent, #000 20%); }
  .ad-large .headline { left: 26px; top: 86px; width: 180px; font-size: 17px; }
  .ad-large .cta { left: 0; top: 247px; width: 204px; height: 33px; border-radius: 0 8px 8px 0; font-size: 13.5px; }
</style>
</head>
<body>

  <section class="ad ad-leaderboard" aria-label="Cabeçalho 728 x 90">
    <div class="silver-arc"></div>
    <div class="product-photo" role="img" aria-label="Foto de toalhas dobradas em tons pastel sobre uma cadeira de madeira"></div>
    <p class="logo">Lar Ventura</p>
    <p class="cta"><span>Confira nossos Produtos</span><span>Exclusivos!</span></p>
    <p class="headline">Sofisticação com exclusividade para sua Casa!</p>
  </section>

  <section class="ad ad-banner" aria-label="Banner 468 x 60">
    <div class="silver-arc"></div>
    <div class="product-photo" role="img" aria-label="Foto de toalhas dobradas em tons pastel sobre uma cadeira de madeira"></div>
    <p class="logo">Lar Ventura</p>
    <p class="cta"><span>Confira nossos Produtos</span><span>Exclusivos!</span></p>
    <p class="headline">Sofisticação com exclusividade para sua Casa!</p>
  </section>

  <section class="ad ad-inline" aria-label="Retângulo inline 300 x 250">
    <div class="silver-arc"></div>
    <div class="product-photo" role="img" aria-label="Foto de toalhas dobradas em tons pastel sobre uma cadeira de madeira"></div>
    <p class="logo">Lar Ventura</p>
    <p class="headline">Sofisticação com exclusividade para sua Casa!</p>
    <p class="cta"><span>Confira nossos Produtos</span><span>Exclusivos!</span></p>
  </section>

  <section class="ad ad-large" aria-label="Retângulo grande 336 x 280">
    <div class="silver-arc"></div>
    <div class="product-photo" role="img" aria-label="Foto de toalhas dobradas em tons pastel sobre uma cadeira de madeira"></div>
    <p class="logo">Lar Ventura</p>
    <p class="headline">Sofisticação com exclusividade para sua Casa!</p>
    <p class="cta"><span>Confira nossos Produtos</span><span>Exclusivos!</span></p>
  </section>

</body>
</html>
```